Premium Food Label Design – High-End Boutique Jar Labels (3 Sizes)

I require a complete jar label redesign across three sizes:
75mm x 130mm (Large & Medium)
55mm x 120mm (Small)
45mm x 120mm (XS)

The design must feel professional, modern, elegant, and high-end boutique.
Primary aesthetic: white, minimal, refined, with accents in soft brown and gold/bronze. (see prefer colours of logo in OLD LABEL PDF)
Transparent background required.

I have attached my current label for wording reference only — I want to move away from the kraft look entirely.
The label must include all existing details, plus a dedicated space to manually add batch number and date.

IMPORTANT: Final files must be supplied as editable Adobe Illustrator (.AI) files with live text layers (not outlined) so I can update them as needed.
Logo is attached. I’m open to a fresh, elevated design direction aligned with a premium brand feel.
Updates

Low design quality

Target Market(s)

People who appreciate high-end, thoughtfully crafted food and are willing to pay for quality

Industry/Entity Type

Gourmet Food / Artisan Food Packaging

Requirements
Must have
• Premium, minimal aesthetic, Strong typography hierarchy, White background, Consistency across 3 sizes
Nice to have
• Elevated “Amber Meadow” styling
Should not have
• No bright or bold colours, No clutter or overcrowding, No heavy borders or thick frames,No “homemade/craft” fonts

```html
<!DOCTYPE html>
<html lang="en">
<head>
<meta charset="utf-8">
<title>Tomato Relish – Jar Label Set</title>
<link href="https://fonts.googleapis.com/css2?family=Montserrat:wght@400;500&family=Quicksand:wght@500;600&family=Lato:wght@400&display=swap" rel="stylesheet">
<style>
  :root {
    --ink-brown: #3d2116;
    --ink-maroon: #5e1616;
    --ink-body: #6a1c1c;
    --frame: #1e1e1e;
    --paper: #ffffff;
    --caption: #222222;
  }
  * { box-sizing: border-box; margin: 0; padding: 0; }
  html, body { width: 1044px; height: 1200px; overflow: hidden; background: var(--paper); }
  .sheet { position: relative; width: 1044px; height: 1200px; }

  .label {
    position: absolute;
    border: 1.4px solid var(--frame);
    background: var(--paper);
    color: var(--ink-maroon);
  }
  .label > * { position: absolute; }
  .label > .centered { left: 0; right: 0; text-align: center; }

  /* sizes */
  .label--large-front  { left: 27px;  top: 59px; width: 264px; height: 457px; }
  .label--large-back   { left: 311px; top: 59px; width: 265px; height: 457px; }
  .label--medium-front { left: 613px; top: 77px; width: 194px; height: 421px; }
  .label--medium-back  { left: 819px; top: 77px; width: 193px; height: 421px; }
  .label--xs-front     { left: 329px; top: 594px; width: 159px; height: 422px; }
  .label--xs-back      { left: 521px; top: 594px; width: 159px; height: 422px; }

  /* front */
  .brand-name {
    font-family: "Montserrat", sans-serif;
    font-weight: 400;
    color: var(--ink-brown);
    letter-spacing: 0.14em;
  }
  .brand-dot {
    left: 50%;
    border-radius: 50%;
    background: var(--ink-brown);
    transform: translateX(-50%);
  }
  .product-title {
    font-family: "Montserrat", sans-serif;
    font-weight: 400;
    letter-spacing: 0.06em;
    color: var(--ink-maroon);
    white-space: nowrap;
  }
  .product-tag {
    font-family: "Montserrat", sans-serif;
    font-weight: 400;
    letter-spacing: 0.1em;
    color: var(--ink-maroon);
  }
  .made-with-love {
    font-family: "Montserrat", sans-serif;
    letter-spacing: 0.08em;
    color: var(--ink-maroon);
    display: flex; justify-content: center; align-items: center;
  }
  .made-with-love .ring {
    display: inline-flex; align-items: center; justify-content: center;
    border: 1.2px solid var(--ink-maroon);
    border-radius: 50%;
    margin: 0 0.15em;
  }
  .weight-rule {
    left: 50%;
    height: 0; border-top: 1px solid var(--ink-maroon);
    transform: translateX(-50%);
  }
  .net-weight {
    font-family: "Montserrat", sans-serif;
    font-weight: 400;
    color: var(--ink-brown);
  }

  /* back */
  .back-dot {
    border-radius: 50%;
    background: var(--ink-brown);
  }
  .back-name {
    text-align: left;
    font-family: "Quicksand", sans-serif;
    font-weight: 600;
    letter-spacing: 0.05em;
    color: var(--ink-body);
    white-space: nowrap;
  }
  .back-copy, .back-footer {
    font-family: "Quicksand", sans-serif;
    font-weight: 600;
    letter-spacing: 0.05em;
    color: var(--ink-body);
  }
  .back-copy p + p, .back-footer p + p { margin-top: 1lh; }

  /* large */
  .label--large-front .brand-name { top: 72px; font-size: 17px; }
  .label--large-front .brand-dot { top: 112px; width: 92px; height: 92px; }
  .label--large-front .product-title { top: 269px; font-size: 23.5px; }
  .label--large-front .product-tag { top: 303px; font-size: 12px; }
  .label--large-front .made-with-love { top: 352px; font-size: 10.5px; }
  .label--large-front .ring { width: 38px; height: 38px; }
  .label--large-front .weight-rule { top: 395px; width: 73px; }
  .label--large-front .net-weight { top: 405px; font-size: 12px; }

  .label--large-back .back-dot { left: 46px; top: 75px; width: 48px; height: 48px; }
  .label--large-back .back-name { left: 95px; top: 117px; font-size: 8.5px; }
  .label--large-back .back-copy { top: 140px; font-size: 8.5px; line-height: 10.4px; }
  .label--large-back .back-footer { top: 381px; font-size: 8.5px; line-height: 10.4px; }

  /* medium */
  .label--medium-front .brand-name { top: 68px; font-size: 12.5px; }
  .label--medium-front .brand-dot { top: 100px; width: 70px; height: 70px; }
  .label--medium-front .product-title { top: 256px; font-size: 17px; }
  .label--medium-front .product-tag { top: 279px; font-size: 9px; }
  .label--medium-front .made-with-love { top: 336px; font-size: 7.8px; }
  .label--medium-front .ring { width: 28px; height: 28px; }
  .label--medium-front .weight-rule { top: 365px; width: 52px; }
  .label--medium-front .net-weight { top: 373px; font-size: 9.5px; }

  .label--medium-back .back-dot { left: 29px; top: 96px; width: 40px; height: 40px; }
  .label--medium-back .back-name { left: 69px; top: 130px; font-size: 7px; }
  .label--medium-back .back-copy { top: 148px; font-size: 7px; line-height: 8.6px; }
  .label--medium-back .back-footer { top: 349px; font-size: 7px; line-height: 8.6px; }

  /* xs */
  .label--xs-front .brand-name { top: 62px; font-size: 10.5px; }
  .label--xs-front .brand-dot { top: 90px; width: 60px; height: 60px; }
  .label--xs-front .product-title { top: 219px; font-size: 15px; }
  .label--xs-front .product-tag { top: 240px; font-size: 7.6px; }
  .label--xs-front .made-with-love { top: 350px; font-size: 6.6px; }
  .label--xs-front .ring { width: 25px; height: 25px; }
  .label--xs-front .weight-rule { top: 377px; width: 45px; }
  .label--xs-front .net-weight { top: 384px; font-size: 8px; }

  .label--xs-back .back-dot { left: 22px; top: 98px; width: 34px; height: 34px; }
  .label--xs-back .back-name { left: 57px; top: 127px; font-size: 6px; }
  .label--xs-back .back-copy { top: 145px; font-size: 5.9px; line-height: 7.7px; }
  .label--xs-back .back-footer { top: 357px; font-size: 5.9px; line-height: 7.7px; }

  .size-notes {
    position: absolute; left: 399px; top: 1077px;
    font-family: "Lato", sans-serif;
    font-size: 13px; line-height: 18px;
    color: var(--caption);
  }
</style>
</head>
<body>
<main class="sheet">

  <!-- Large / medium jar, 75 × 130 mm -->
  <section class="label label--large-front">
    <div class="brand-name centered">HEARTH HARVEST</div>
    <div class="brand-dot"></div>
    <h1 class="product-title centered">TOMATO RELISH</h1>
    <div class="product-tag centered">POPULAR CHOICE</div>
    <div class="made-with-love centered">MADE<span class="ring">WITH</span>LOVE</div>
    <div class="weight-rule"></div>
    <div class="net-weight centered">375 G</div>
  </section>

  <section class="label label--large-back">
    <div class="back-dot"></div>
    <div class="back-name">Amber Meadow</div>
    <div class="back-copy centered">
      <p>What is made with love is felt in return.<br>May this relish nourish more than the<br>meal –<br>bringing comfort, connection, and joy<br>to every moment shared.</p>
      <p>Ingredients:<br>Tomatoes, onion, sugar, vinegar, salt,<br>spices, thickener (cornflour)</p>
      <p>STORAGE: KEEP REFRIGERATED ONCE<br>OPENED</p>
      <p>Batch: _______<br>Date: _______</p>
    </div>
    <div class="back-footer centered">
      <p>Made by Hearth Harvest QLD, Australia<br>www.hearthharvest.com</p>
      <p>info@hearthharvest.com</p>
    </div>
  </section>

  <!-- Small jar, 55 × 120 mm -->
  <section class="label label--medium-front">
    <div class="brand-name centered">HEARTH HARVEST</div>
    <div class="brand-dot"></div>
    <h1 class="product-title centered">TOMATO RELISH</h1>
    <div class="product-tag centered">POPULAR CHOICE</div>
    <div class="made-with-love centered">MADE<span class="ring">WITH</span>LOVE</div>
    <div class="weight-rule"></div>
    <div class="net-weight centered">375 G</div>
  </section>

  <section class="label label--medium-back">
    <div class="back-dot"></div>
    <div class="back-name">Amber Meadow</div>
    <div class="back-copy centered">
      <p>What is made with love is felt in return.<br>May this relish nourish more than the<br>meal –<br>bringing comfort, connection, and joy<br>to every moment shared.</p>
      <p>Ingredients:<br>Tomatoes, onion, sugar, vinegar, salt,<br>spices, thickener (cornflour)</p>
      <p>STORAGE: KEEP REFRIGERATED ONCE<br>OPENED</p>
      <p>Batch: _______<br>Date: _______</p>
    </div>
    <div class="back-footer centered">
      <p>Made by Hearth Harvest QLD, Australia<br>www.hearthharvest.com</p>
      <p>info@hearthharvest.com</p>
    </div>
  </section>

  <!-- XS jar, 45 × 120 mm -->
  <section class="label label--xs-front">
    <div class="brand-name centered">HEARTH HARVEST</div>
    <div class="brand-dot"></div>
    <h1 class="product-title centered">TOMATO RELISH</h1>
    <div class="product-tag centered">POPULAR CHOICE</div>
    <div class="made-with-love centered">MADE<span class="ring">WITH</span>LOVE</div>
    <div class="weight-rule"></div>
    <div class="net-weight centered">375 G</div>
  </section>

  <section class="label label--xs-back">
    <div class="back-dot"></div>
    <div class="back-name">Amber Meadow</div>
    <div class="back-copy centered">
      <p>What is made with love is felt in return.<br>May this relish nourish more than the<br>meal –<br>bringing comfort, connection, and joy<br>to every moment shared.</p>
      <p>Ingredients:<br>Tomatoes, onion, sugar, vinegar, salt,<br>spices, thickener (cornflour)</p>
      <p>STORAGE: KEEP REFRIGERATED ONCE<br>OPENED</p>
      <p>Batch: _______<br>Date: _______</p>
    </div>
    <div class="back-footer centered">
      <p>Made by Hearth Harvest QLD, Australia<br>www.hearthharvest.com</p>
      <p>info@hearthharvest.com</p>
    </div>
  </section>

  <div class="size-notes">
    75 mm x 130 mm (grande e medio)<br>
    55 mm x 120 mm (piccolo)<br>
    45 mm x 120 mm (XS)
  </div>
</main>
</body>
</html>
```